Etiketten-Design für fassgelagerten Rum
Zielgruppe
Wir stellen bisher 3 flavored Rum Sorten her (www.ostwindbrand.com) und benötigen ein neues Etikett für unseren fassgelagerten Rum ohne weitere Zusätze wie Zucker oder Aromen.
Die Zuckerrohrmelasse wird gebrannt und anschließend in unsere eigenen Fässer gefüllt. Momentan haben wir Eichenfässer und Maulbeerbaumfässer belegt mit unserem Rohbrand aus Südamerika.
Die Etiketten kommen auf eine hochwertige Flasche mit 500ml Fassungsvermögen (Flasche Vardo 500ml)
Die Preise pro Flasche werden bei ca. 30-40€ liegen, also eher im höheren Preissegment.
Unsere bisherige Zielgruppe ist breit gefächert von 30-50 Jahren, sowohl männliche als auch weibliche Kunden trinken unseren Rum.
Aufgabenstellung
Es soll ein Grunddesign für den fassgelagerten Rum geben, welche farblich und/oder durch das verwendete Fass zur Lagerung zu unterscheiden ist. Das Kerndesign soll aber beibehalten werden.
Zuckerrohr: aus Südamerika
Fasssorten: Eichenfass, Maulbeerbaumfass
Sollten zur Unterscheidung der „Rumfasssorten“ einzelne Grafiken oder Bilder eingefügt werden, sollen diese bei weiteren Sorten problemlos über ein Vektorenprogramm getauscht werden können, ohne dass es das Gesamtbild verschlechtert.
Design für die 500ml Flasche Etikett Vorder-und Rückseite – ca. Etikettenmaße (kann auch etwas größer sein) : Länge 79mm x 60mm (kann auch geringfügig größer sein, sollte aber auf die Flasche passen), wenn Ideen bestehen nur ein Etikett zu verwenden dafür etwas breiter, wäre das auch okay, ist aber kein muss.
Das Design soll in vereinfachter Form auch für Flasche: Vardo 50ml - Etikettenmaße Länge 65mm x Breite 38mm vorhanden sein.
Das Design soll hochwertig, modern und edel aussehen. Es kann auch gerne schlicht gehalten werden, sollte aber beim Kunden den Wunsch/Gedanken einbringen dieses Produkt erinnert mich an meinen Karibikurlaub, das muss ich haben. Ein Eyecatcher, dass sich von den bisherigen Rum Produkten auf dem Markt abhebt und im Regal auffällt.
Es soll auf jeden Fall nicht altmodisch wirken, da wir ein modernes, junges Startup-Unternehmen sind.
Auf dem Etikett/Etiketten müssen folgende Angaben unterbracht werden:
Vorderseite 500ml:
-Firmenlogo (siehe Anhang)
-Alkoholgehalt bspw. 42% / 84-Proof
-Füllmenge 500ml
- Produktname: 9th , 17th
-Fassgelagert
-Handelsbezeichnung: handcrafted Rum
-Bottle No. 1/120 (die Zahlen werden von Hand geschrieben)
-Batch No.1 (Zahl wird von Hand geschrieben) kann auch auf die Rückseite
Rückseite 500ml:
-EAN-Code
-QR-Code siehe Anhang
-www.ostwindbrand.com
-#ostwindbrand (falls der Platz vorhanden ist und es gut zu integrieren ist)..

```html
<!DOCTYPE html>
<html lang="de">
<head>
<meta charset="utf-8">
<title>Ostwind 9th – Etikettenvarianten</title>
<link href="https://fonts.googleapis.com/css2?family=Big+Shoulders+Display:wght@500;600;700&family=Montserrat:wght@400&family=Oswald:wght@500&family=Roboto:wght@400&display=swap" rel="stylesheet">
<style>
  :root{
    --stage-top:#c4c5c7;
    --stage-mid:#e6e7e8;
    --label-dark:#000000;
    --label-light:#ffffff;
    --gold:#c8943f;
    --gold-light:#f1d39a;
    --gold-deep:#8f5a22;
    --blue:#1aa3e0;
    --ink:#1c1c1c;
    --line-gold:#a86f2c;
    --faint-dark:rgba(255,255,255,0.09);
    --faint-light:rgba(0,0,0,0.06);
  }
  *{margin:0;padding:0;box-sizing:border-box}
  html,body{width:1200px;height:665px;overflow:hidden}
  body{
    background:linear-gradient(180deg,var(--stage-top) 0%,var(--stage-mid) 60%,var(--stage-top) 100%);
    position:relative;
    font-family:"Roboto",Arial,sans-serif;
  }
  .label{
    position:absolute;top:54px;width:367px;height:558px;
    border-radius:9px;overflow:hidden;
    background:var(--label-dark);color:#fff;
  }
  .label--gold{left:39px}
  .label--mono{left:417px}
  .label--light{left:794px;background:var(--label-light);color:var(--ink);border:1px solid #cfcfcf}

  .backdrop{
    position:absolute;left:0;top:230px;width:367px;height:328px;
    background:radial-gradient(ellipse at 85% 30%,var(--faint-dark) 0%,transparent 55%),
               radial-gradient(ellipse at 15% 65%,var(--faint-dark) 0%,transparent 55%);
  }
  .label--light .backdrop{
    background:radial-gradient(ellipse at 85% 30%,var(--faint-light) 0%,transparent 55%),
               radial-gradient(ellipse at 15% 65%,var(--faint-light) 0%,transparent 55%);
  }

  .brand-disc{
    position:absolute;left:120px;top:24px;width:121px;height:121px;border-radius:50%;
    background:linear-gradient(135deg,var(--gold-light),var(--gold) 55%,var(--gold-deep));
    opacity:.9;
  }
  .label--light .brand-disc{background:linear-gradient(135deg,#fff8e6,var(--gold-light) 60%,#e4bd72)}
  .brand-name{
    position:absolute;left:81px;top:118px;width:198px;height:31px;
    font-family:"Big Shoulders Display",sans-serif;font-weight:600;
    font-size:30px;line-height:31px;letter-spacing:9px;text-align:center;
    color:var(--gold);
  }
  .brand-rule{position:absolute;left:82px;top:160px;width:196px;height:2px;background:#fff}
  .label--light .brand-rule{background:var(--ink)}

  .ribbon{position:absolute;width:220px;height:42px}
  .ribbon svg{position:absolute;inset:0}
  .ribbon__text{
    position:absolute;inset:0;display:flex;align-items:center;justify-content:center;
    font-family:"Big Shoulders Display",sans-serif;font-weight:600;font-size:28px;line-height:1;
    color:var(--blue);letter-spacing:.3px;white-space:nowrap;
  }
  .ribbon--top{left:69px;top:179px}
  .ribbon--top .ribbon__text{padding-left:20px}
  .ribbon--bottom{left:79px;top:400px}
  .ribbon--bottom .ribbon__text{padding-right:18px}

  .product-frame{
    position:absolute;left:79px;top:231px;width:210px;height:160px;
    border:3px solid #fff;
  }
  .label--gold .product-frame{border-color:var(--gold)}
  .label--light .product-frame{border-color:#3a3a3a}
  .product-name{
    position:absolute;left:0;right:0;top:4px;text-align:center;
    font-family:"Big Shoulders Display",sans-serif;font-weight:700;
    font-size:134px;line-height:124px;letter-spacing:2px;color:#fff;
  }
  .label--gold .product-name,.label--light .product-name{color:var(--gold)}
  .product-cask{
    position:absolute;left:0;right:0;bottom:4px;text-align:center;
    font-family:"Montserrat",sans-serif;font-size:13px;letter-spacing:5px;color:#fff;
  }
  .label--light .product-cask{color:var(--ink)}

  .fill-rule{position:absolute;left:24px;width:319px;height:1px;background:#fff}
  .fill-rule--top{top:463px}
  .fill-rule--bottom{top:527px}
  .label--gold .fill-rule{background:var(--line-gold)}
  .label--light .fill-rule{background:#555}

  .fill-field{position:absolute;top:474px;font-size:15px}
  .fill-field__caption{height:16px;line-height:16px}
  .fill-field--bottle{left:34px}
  .fill-field--batch{right:34px;text-align:right}
  .fill-line{position:absolute;left:34px;top:490px;width:299px;height:22px;background:#fff}
  .label--light .fill-field{top:469px}
  .label--light .fill-field__caption{background:#2a2a2a;color:#fff;height:20px;line-height:20px;padding:0 5px}
  .label--light .fill-field--bottle{left:34px;width:150px}
  .label--light .fill-field--batch{right:34px;width:150px}
  .label--light .fill-line{top:489px;border:1px solid #777;border-top:none;height:22px}

  .strength-badge{position:absolute;left:133px;top:458px;width:102px;height:76px}
  .strength-badge svg{position:absolute;inset:0}
  .strength-badge__text{
    position:absolute;inset:0;display:flex;flex-direction:column;align-items:center;justify-content:center;
    font-family:"Oswald",sans-serif;font-weight:500;font-size:15px;line-height:19px;color:#fff;
    transform:scaleX(.8);
  }
  .label--light .strength-badge__text{color:var(--ink)}
</style>
</head>
<body>

<section class="label label--gold">
  <div class="backdrop" role="img" aria-label="Dezente Palmensilhouetten im Hintergrund"></div>
  <div class="brand-disc"></div>
  <div class="brand-name">OSTWIND</div>
  <div class="brand-rule"></div>
  <div class="ribbon ribbon--top">
    <svg viewBox="0 0 220 42"><polygon points="1.5,1.5 218.5,1.5 218.5,40.5 1.5,40.5 16,21" fill="none" stroke="var(--blue)" stroke-width="3"/></svg>
    <div class="ribbon__text">• FASSGELAGERT</div>
  </div>
  <div class="product-frame">
    <div class="product-name">9TH</div>
    <div class="product-cask">ELM BARREL</div>
  </div>
  <div class="ribbon ribbon--bottom">
    <svg viewBox="0 0 220 42"><polygon points="1.5,1.5 218.5,1.5 204,21 218.5,40.5 1.5,40.5" fill="none" stroke="var(--blue)" stroke-width="3"/></svg>
    <div class="ribbon__text">HANDCRAFTED RUM •</div>
  </div>
  <div class="fill-rule fill-rule--top"></div>
  <div class="fill-field fill-field--bottle"><div class="fill-field__caption">Botlle No.</div></div>
  <div class="fill-field fill-field--batch"><div class="fill-field__caption">Batch No.</div></div>
  <div class="fill-line"></div>
  <div class="fill-rule fill-rule--bottom"></div>
  <div class="strength-badge">
    <svg viewBox="0 0 102 76"><rect x="2" y="6" width="98" height="64" rx="30" fill="#000" stroke="var(--gold)" stroke-width="2"/><rect x="7" y="11" width="88" height="54" rx="25" fill="none" stroke="var(--gold)" stroke-width="1"/></svg>
    <div class="strength-badge__text"><span>42%Vol.</span><span>84Proof-500ml</span></div>
  </div>
</section>

<section class="label label--mono">
  <div class="backdrop" role="img" aria-label="Dezente Palmensilhouetten im Hintergrund"></div>
  <div class="brand-disc"></div>
  <div class="brand-name">OSTWIND</div>
  <div class="brand-rule"></div>
  <div class="ribbon ribbon--top">
    <svg viewBox="0 0 220 42"><polygon points="1.5,1.5 218.5,1.5 218.5,40.5 1.5,40.5 16,21" fill="none" stroke="var(--blue)" stroke-width="3"/></svg>
    <div class="ribbon__text">• FASSGELAGERT</div>
  </div>
  <div class="product-frame">
    <div class="product-name">9TH</div>
    <div class="product-cask">ELM BARREL</div>
  </div>
  <div class="ribbon ribbon--bottom">
    <svg viewBox="0 0 220 42"><polygon points="1.5,1.5 218.5,1.5 204,21 218.5,40.5 1.5,40.5" fill="none" stroke="var(--blue)" stroke-width="3"/></svg>
    <div class="ribbon__text">HANDCRAFTED RUM •</div>
  </div>
  <div class="fill-rule fill-rule--top"></div>
  <div class="fill-field fill-field--bottle"><div class="fill-field__caption">Botlle No.</div></div>
  <div class="fill-field fill-field--batch"><div class="fill-field__caption">Batch No.</div></div>
  <div class="fill-line"></div>
  <div class="fill-rule fill-rule--bottom"></div>
  <div class="strength-badge">
    <svg viewBox="0 0 102 76"><rect x="2" y="6" width="98" height="64" rx="30" fill="#000" stroke="#fff" stroke-width="2"/><rect x="7" y="11" width="88" height="54" rx="25" fill="none" stroke="#fff" stroke-width="1"/></svg>
    <div class="strength-badge__text"><span>42%Vol.</span><span>84Proof-500ml</span></div>
  </div>
</section>

<section class="label label--light">
  <div class="backdrop" role="img" aria-label="Dezente Palmensilhouetten im Hintergrund"></div>
  <div class="brand-disc"></div>
  <div class="brand-name">OSTWIND</div>
  <div class="brand-rule"></div>
  <div class="ribbon ribbon--top">
    <svg viewBox="0 0 220 42"><polygon points="1.5,1.5 218.5,1.5 218.5,40.5 1.5,40.5 16,21" fill="none" stroke="var(--blue)" stroke-width="3"/></svg>
    <div class="ribbon__text">• FASSGELAGERT</div>
  </div>
  <div class="product-frame">
    <div class="product-name">9TH</div>
    <div class="product-cask">ELM BARREL</div>
  </div>
  <div class="ribbon ribbon--bottom">
    <svg viewBox="0 0 220 42"><polygon points="1.5,1.5 218.5,1.5 204,21 218.5,40.5 1.5,40.5" fill="none" stroke="var(--blue)" stroke-width="3"/></svg>
    <div class="ribbon__text">HANDCRAFTED RUM •</div>
  </div>
  <div class="fill-rule fill-rule--top"></div>
  <div class="fill-field fill-field--bottle"><div class="fill-field__caption">Botlle No.</div></div>
  <div class="fill-field fill-field--batch"><div class="fill-field__caption">Batch No.</div></div>
  <div class="fill-line"></div>
  <div class="fill-rule fill-rule--bottom"></div>
  <div class="strength-badge">
    <svg viewBox="0 0 102 76"><rect x="2" y="6" width="98" height="64" rx="30" fill="#fff" stroke="#333" stroke-width="2"/><rect x="7" y="11" width="88" height="54" rx="25" fill="none" stroke="#333" stroke-width="1"/></svg>
    <div class="strength-badge__text"><span>42%Vol.</span><span>84Proof-500ml</span></div>
  </div>
</section>

</body>
</html>
```